Bright Meadow Counseling Business Card design with a visually interesting use of Space

I need business cards that are luxurious and give a peaceful, calm vibe. I also had some letterhead designed, and i like the look of it also, it's attached with the logo design for reference/ ideas but feel free to be creative.

Target Market(s)

High end luxurious client who needs counseling

Industry/Entity Type

Marriage and Family Therapy

Contact Information for Business Card

Mira Kowalczyk MS LMFT/ or Toby Hallett address 4150 Larkin Suite 600

Font styles to use
Sans Serif

Colors
0054AA
0677BA
7BADD7
CADEEF
E8F1F8
0094D4
00A9DD
6FCCEA
C7EBF8
E9F6FB
A7469A
B969AE
D3A5CF
EDDBEB
F8F0F9
6B429C
8869AF
B7A5CE
E3DAEB
F3F0F8

Requirements
Must have
• Logo and color scheme but be simple modern and luxurious
Nice to have
• I'd like to incorporate some elelmets from the logo and letterhead into a simple modern card

```html
<!DOCTYPE html>
<html lang="en">
<head>
<meta charset="utf-8">
<title>Bright Meadow Counseling – Business Card</title>
<link href="https://fonts.googleapis.com/css2?family=Lato:wght@300;400;700&display=swap" rel="stylesheet">
<style>
  :root {
    --backdrop: #2b2b2d;
    --card: #0c0c0d;
    --card-edge: #1a1a1c;
    --ink: #ffffff;
    --ink-soft: #e6e6e8;
    --icon-blue: #0677BA;
    --divider: #4a4a4e;
    --accent-violet: #8869AF;
  }
  * { box-sizing: border-box; margin: 0; padding: 0; }
  html, body {
    width: 1200px; height: 900px; overflow: hidden;
    background: var(--backdrop);
    font-family: "Lato", Arial, sans-serif;
  }
  .sheet {
    width: 1200px; height: 900px;
    display: flex; flex-direction: column;
    align-items: center; justify-content: center; gap: 40px;
  }
  .card {
    width: 665px; height: 380px;
    background: var(--card);
    border: 1px solid var(--card-edge);
    position: relative;
    box-shadow: 0 18px 40px rgba(0,0,0,.5);
  }
  .brand {
    display: flex; align-items: center; gap: 14px;
    color: var(--ink);
    font-weight: 300;
    font-size: 28px;
    line-height: 1.2;
    letter-spacing: 1px;
  }
  .brand-dot {
    width: 14px; height: 14px; border-radius: 50%;
    background: var(--accent-violet);
    flex: none;
  }
  .brand-name span { display: block; }
  /* front: brand + contact */
  .card--front .brand {
    position: absolute; left: 56px; top: 156px;
    width: 290px;
  }
  .card--front .divider {
    position: absolute; left: 372px; top: 92px;
    width: 1px; height: 196px; background: var(--divider);
  }
  .contact {
    position: absolute; left: 402px; top: 104px;
    color: var(--ink-soft);
  }
  .contact-name {
    font-weight: 700; font-size: 24px; color: var(--ink);
    margin-bottom: 16px;
  }
  .contact-list { list-style: none; }
  .contact-list li {
    display: flex; align-items: center; gap: 10px;
    font-size: 15.5px; line-height: 1; margin-bottom: 12px;
  }
  .contact-list li.address { margin-top: 10px; }
  .contact-list svg { width: 16px; height: 16px; flex: none; fill: var(--icon-blue); }
  /* back: brand only */
  .card--back .brand {
    position: absolute; left: 0; right: 0; top: 156px;
    justify-content: center;
  }
</style>
</head>
<body>
<main class="sheet">
  <section class="card card--back" aria-label="Card back">
    <div class="brand"><span class="brand-dot"></span><p class="brand-name"><span>Bright Meadow</span><span>Counseling</span></p></div>
  </section>

  <section class="card card--front" aria-label="Card front">
    <div class="brand"><span class="brand-dot"></span><p class="brand-name"><span>Bright Meadow</span><span>Counseling</span></p></div>
    <div class="divider"></div>
    <div class="contact">
      <p class="contact-name">Toby Hallett</p>
      <ul class="contact-list">
        <li>
          <svg viewBox="0 0 24 24" aria-hidden="true"><path d="M6.6 10.8a15.1 15.1 0 0 0 6.6 6.6l2.2-2.2c.3-.3.7-.4 1-.2 1.1.4 2.3.6 3.6.6.6 0 1 .4 1 1V20c0 .6-.4 1-1 1A17 17 0 0 1 3 4c0-.6.4-1 1-1h3.5c.6 0 1 .4 1 1 0 1.3.2 2.5.6 3.6.1.3 0 .7-.2 1z"/></svg>
          5550147720
        </li>
        <li>
          <svg viewBox="0 0 24 24" aria-hidden="true"><path d="M2 5h20v14H2zm2 2v.5l8 5 8-5V7zm0 2.8V17h16V9.8l-8 5z"/></svg>
          info@brightmeadow.com
        </li>
        <li>
          <svg viewBox="0 0 24 24" aria-hidden="true"><path d="M12 2a10 10 0 1 0 0 20 10 10 0 0 0 0-20zm6.9 9h-3a15 15 0 0 0-1.3-6A8 8 0 0 1 18.9 11zM12 4c1 1.3 1.8 3.8 2 7h-4c.2-3.2 1-5.7 2-7zM9.4 5a15 15 0 0 0-1.3 6h-3A8 8 0 0 1 9.4 5zM5.1 13h3a15 15 0 0 0 1.3 6 8 8 0 0 1-4.3-6zM12 20c-1-1.3-1.8-3.8-2-7h4c-.2 3.2-1 5.7-2 7zm2.6-1a15 15 0 0 0 1.3-6h3a8 8 0 0 1-4.3 6z"/></svg>
          www.brightmeadow.com
        </li>
        <li class="address">
          <svg viewBox="0 0 24 24" aria-hidden="true"><path d="M12 2a7 7 0 0 0-7 7c0 5 7 13 7 13s7-8 7-13a7 7 0 0 0-7-7zm0 9.5A2.5 2.5 0 1 1 12 6.5a2.5 2.5 0 0 1 0 5z"/></svg>
          4150 Larkin Suite 600
        </li>
      </ul>
    </div>
  </section>
</main>
</body>
</html>
```